Values and Organizational Purpose Signage

We recently solidified our company values, organizatioanal purpose and strategic vision. I'd like to develop some tasteful (not overly corporate) signage of these values to display in our office.

I've attached the hand-written values and purpose that my core team members then initialed acknowleding they align along with the signage at the front of our office to provide some perspective on our brand identity.

Industry/Entity Type

It Company

Font styles to use
Sans Serif

Requirements
Must have
• I'd like to see the values and org purpose depicted as one sign and as separate signs (i.e., values on one sign and org purpose on another). I need it to reflect our brand identity which I've uploaded

```html
<!DOCTYPE html>
<html lang="en">
<head>
<meta charset="utf-8">
<title>Organizational Purpose – Arvenna</title>
<link rel="stylesheet" href="https://fonts.googleapis.com/css2?family=Source+Serif+4:opsz,wght@8..60,300;8..60,400;8..60,600&display=swap">
<style>
  :root {
    --frame-green: #c3d62b;
    --tagline-green: #c1d52e;
    --ink-dark: #2b2d31;
    --heading-slate: #434c57;
    --rule-grey: #6b6f73;
    --paper: #ffffff;
  }
  html, body {
    margin: 0;
    padding: 0;
    width: 730px;
    height: 1200px;
    overflow: hidden;
    background: var(--paper);
  }
  .sign {
    position: relative;
    width: 730px;
    height: 1200px;
    box-sizing: border-box;
    border: 11px solid var(--frame-green);
    background: var(--paper);
    font-family: "Source Serif 4", Georgia, serif;
  }
  .brand {
    position: absolute;
    top: 96px;
    left: 0;
    right: 0;
    display: flex;
    justify-content: center;
    align-items: center;
    gap: 12px;
  }
  .brand-name {
    font-size: 40px;
    font-weight: 600;
    color: var(--ink-dark);
    letter-spacing: 1px;
    line-height: 1;
  }
  .brand-dot {
    width: 14px;
    height: 14px;
    background: var(--frame-green);
  }
  .tagline {
    position: absolute;
    top: 386px;
    left: 127px;
    margin: 0;
    font-size: 46px;
    font-weight: 300;
    line-height: 58px;
    color: var(--tagline-green);
  }
  .divider {
    position: absolute;
    top: 578px;
    left: 138px;
    width: 368px;
    height: 3px;
    background: var(--rule-grey);
  }
  .title {
    position: absolute;
    top: 576px;
    left: 52px;
    margin: 0;
    font-size: 92px;
    font-weight: 400;
    line-height: 116px;
    color: var(--heading-slate);
  }
</style>
</head>
<body>
  <main class="sign">
    <div class="brand">
      <span class="brand-name">Arvenna</span>
      <span class="brand-dot"></span>
    </div>
    <p class="tagline">We deliver simple and<br>digestible solutions to<br>complex matters.</p>
    <div class="divider"></div>
    <h1 class="title">Organizational<br>Purpose</h1>
  </main>
</body>
</html>
```